Wine Label for a syrah wine hand crafted from walla walla valley, washington

design a wine label for the name of the brand: Lumaret. It is a wine hand crafted from Walla Walla Valley in Washington state. the label should be landscape in design, 95 mm wide by 85 mm tall. it should include the name of the brand, Lumaret, Walla Walla Valley, 2020 and Syrah. the brand is called lumaret with this in mind:

-lumaret Definition & Meaning |
1. : having (something) at the center. The solar system is helio lumaret, meaning that the sun is at its center. 2. : having (something) as a central interest, influence, subject, in the case of this wine label it is Syrah wine from Walla Walla Valley
this american vitculture area is known for wines which showcase the terrior of the area - this wine is specifically from the Rocks district where there are lots of rocks in the vineyard. think terrior, rocks, dirt, grapes that are hand crafted into a bottle of wine that will cost $125 each.

Target Market(s)

syrah lovers, Rhone valley wine lovers,

Industry/Entity Type

wine industry

Font styles to use
Sans Serif
Other font styles liked:
• freightbig in light, book and medium weights

Requirements
Must have
• the elements described in the project description, please use FreightBig font found on brivant site, light, book and medium weights
Nice to have
• a cool edgy design but elegant a the same time
Should not have
• stock pictures

```html
<!DOCTYPE html>
<html lang="en">
<head>
<meta charset="utf-8">
<title>Lumaret Syrah 2020 Label</title>
<link href="https://fonts.googleapis.com/css2?family=Jost:wght@200;300&family=Libre+Caslon+Text:wght@700&display=swap" rel="stylesheet">
<style>
  :root {
    --backdrop: #e6e6e4;
    --label-cream: #fdfde9;
    --ink: #1f1f1f;
    --ink-soft: #2c2c2c;
    --rule-green: #2f9a35;
    --core-dark: #2a0000;
    --wine-red: #8a0c02;
    --burnt-orange: #df6a12;
    --amber: #e5a04a;
    --pale-amber: #f8c97f;
    --stone-grey: #bcbca8;
  }
  html, body {
    margin: 0;
    padding: 0;
    width: 1200px;
    height: 900px;
    overflow: hidden;
    background: var(--backdrop);
  }
  .canvas {
    position: relative;
    width: 1200px;
    height: 900px;
  }
  .wine-label {
    position: absolute;
    left: 120px;
    top: 20px;
    width: 960px;
    height: 860px;
    background: var(--label-cream);
    box-shadow: 0 6px 24px rgba(0,0,0,0.12);
  }
  .brand-name {
    position: absolute;
    top: 40px;
    left: 0;
    width: 100%;
    margin: 0;
    text-align: center;
    font-family: "Jost", sans-serif;
    font-weight: 200;
    font-size: 52px;
    letter-spacing: 0.62em;
    text-indent: 0.62em;
    color: var(--ink);
    line-height: 1;
  }
  .rings-artwork {
    position: absolute;
    left: 178px;
    top: 119px;
    width: 620px;
    height: 620px;
  }
  .varietal-row {
    position: absolute;
    left: 284px;
    top: 752px;
    width: 389px;
    display: flex;
    justify-content: space-between;
    align-items: flex-end;
    font-family: "Jost", sans-serif;
    font-weight: 300;
    font-size: 25px;
    letter-spacing: -0.02em;
    color: var(--ink-soft);
    line-height: 1;
    padding-bottom: 4px;
    border-bottom: 2px solid var(--rule-green);
  }
  .appellation {
    position: absolute;
    top: 799px;
    left: 0;
    width: 100%;
    margin: 0;
    text-align: center;
    font-family: "Libre Caslon Text", serif;
    font-weight: 700;
    font-size: 13px;
    letter-spacing: 0.08em;
    color: var(--ink);
    text-transform: uppercase;
  }
</style>
</head>
<body>
  <main class="canvas">
    <section class="wine-label">
      <h1 class="brand-name">LUMARET</h1>

      <svg class="rings-artwork" viewBox="0 0 620 620" role="img"
           aria-label="Abstract artwork of overlapping concentric ring segments in deep wine red, burnt orange, amber and stone grey around a dark centre">
        <defs>
          <radialGradient id="ringsTone" cx="50%" cy="50%" r="50%">
            <stop offset="0%" stop-color="var(--core-dark)"/>
            <stop offset="22%" stop-color="var(--core-dark)"/>
            <stop offset="38%" stop-color="var(--wine-red)"/>
            <stop offset="58%" stop-color="var(--burnt-orange)"/>
            <stop offset="78%" stop-color="var(--amber)"/>
            <stop offset="92%" stop-color="var(--pale-amber)"/>
            <stop offset="100%" stop-color="var(--stone-grey)"/>
          </radialGradient>
        </defs>
        <circle cx="310" cy="310" r="308" fill="url(#ringsTone)"/>
      </svg>

      <div class="varietal-row">
        <span class="varietal">SYRAH</span>
        <span class="vintage">2020</span>
      </div>
      <p class="appellation">Walla Walla Valley, Washington State</p>
    </section>
  </main>
</body>
</html>
```